Business Card Design

This is a new business We need a business card that shows that we can do whatever people require for maintaining a building we all so like to Achieve a green star feel about the card and Eco Friendly Properly maintenance Building & Construction cleaning,Carpet Cleaning ,Pressure Cleaning Move in Move Out CleaningRubbish RemovalLawn Mowing & Edging>Who we serveCommercial DevelopersResidential BuildersProperty ManagersBuilding Owners Home Owners Real Estate Agents

Target Market(s)

Building & construction

Industry/Entity Type

Property Maintenance

Contact Information for Business Card

Lindenfall Property Maintenance Colin Marsworth Unit 3 / 8 Tamble Road Hastings 3915Victoria Australia Ph 0487365902

Font styles to use
Sans Serif
Script

Colors
9ccb3b
aaaaaa

Requirements
Must have
• Have eco friendly feel

```html
<!DOCTYPE html>
<html lang="en">
<head>
<meta charset="utf-8">
<title>Lindenfall Property Maintenance – Business Card</title>
<link href="https://fonts.googleapis.com/css2?family=Source+Sans+3:wght@400;600&display=swap" rel="stylesheet">
<style>
  :root {
    --backdrop: #3a3a3a;
    --card: #141414;
    --card-edge: #1e1e1e;
    --green: #9ccb3b;
    --text-light: #e6e6e6;
    --divider: #2c2c2c;
  }
  html, body {
    margin: 0;
    width: 1200px;
    height: 900px;
    overflow: hidden;
    background: var(--backdrop);
    font-family: "Source Sans 3", Arial, sans-serif;
  }
  .canvas {
    width: 1200px;
    height: 900px;
    display: flex;
    align-items: center;
    justify-content: center;
    gap: 48px;
  }
  .card {
    width: 525px;
    height: 300px;
    background: var(--card);
    border-radius: 22px;
    box-shadow: 0 18px 40px rgba(0,0,0,0.45);
    box-sizing: border-box;
    position: relative;
    overflow: hidden;
  }
  .card--front {
    display: flex;
  }
  .brand-panel {
    width: 50%;
    display: flex;
    flex-direction: column;
    align-items: center;
    justify-content: center;
    gap: 18px;
  }
  .brand-mark {
    width: 118px;
    height: 118px;
    border: 3px solid var(--green);
    border-radius: 50%;
    box-sizing: border-box;
  }
  .brand-name {
    color: var(--green);
    font-weight: 600;
    font-size: 21px;
    line-height: 1.15;
    text-align: center;
    margin: 0;
  }
  .divider {
    width: 1px;
    margin: 40px 0;
    background: var(--divider);
  }
  .contact-panel {
    flex: 1;
    padding: 70px 0 0 34px;
    color: var(--text-light);
  }
  .contact-name {
    color: var(--green);
    font-weight: 600;
    font-size: 20px;
    margin: 0 0 12px;
  }
  .contact-address {
    font-style: normal;
    font-size: 15px;
    line-height: 1.35;
    margin: 0 0 16px;
  }
  .contact-phone {
    display: flex;
    align-items: center;
    gap: 10px;
    font-size: 16px;
    margin: 0;
  }
  .card--back {
    display: flex;
    flex-direction: column;
    align-items: center;
    justify-content: center;
    gap: 20px;
  }
  .card--back .brand-mark {
    width: 150px;
    height: 150px;
  }
</style>
</head>
<body>
<main class="canvas">
  <section class="card card--front">
    <div class="brand-panel">
      <div class="brand-mark" aria-hidden="true"></div>
      <p class="brand-name">Lindenfall<br>Property Maintenance</p>
    </div>
    <div class="divider"></div>
    <div class="contact-panel">
      <h1 class="contact-name">Colin Marsworth</h1>
      <address class="contact-address">
        Unit 3 / 8 Tamble Road<br>
        Orvale 3862<br>
        Victoria Australia
      </address>
      <p class="contact-phone">
        <svg width="10" height="15" viewBox="0 0 10 15" aria-hidden="true">
          <rect x="1" y="1" width="8" height="13" rx="1.5" fill="none" stroke="#9ccb3b" stroke-width="1.5"/>
          <line x1="4" y1="11.5" x2="6" y2="11.5" stroke="#9ccb3b" stroke-width="1.2"/>
        </svg>
        0487365902
      </p>
    </div>
  </section>
  <section class="card card--back">
    <div class="brand-mark" aria-hidden="true"></div>
    <p class="brand-name">Lindenfall Property Maintenance</p>
  </section>
</main>
</body>
</html>
```